New Business Card Design for Business Consulting Business

We need a business card design that reflects the simplicity of our business. We partner with our clients to help them deliver change. We are a different kind of business consulting group. We don't just provide you with the theory. We provide you with the leadership and capability to execute change.

Vonduro is a professional services organisation that partners with their clients to lead the execution of strategic process and system improvement initiatives. Vonduro combines hands on delivery with coaching in best practice methodologies and approaches to build their clients capabilities to ensure their ongoing success in project implementations. Vonduro offers business advisory services in Project Management, Business Process Management, Change Management and Business Analytics.

Reason: Hi Designers, Thanks for all of your great designs. There are some really creative and cool ideas. Everyone is really capturing the essence of my business Vonduro. I am extending the deadline for the business card design by 6 days as I need to consult my Marketing colleague who won't be back in Australia until Wednesday. I would like to sit down with them and review all of the best designs. The key themes of the things I have really liked on my first review are: 1) Capturing the company website on the back of the card. 2) Including the company logo on the back of the card too. 3) Including the types of services on the back of the card that the company offers - Project Management - Business Process Management - Change Management - Business Analytics 4) Utilising some images on the back of the card Just so everyone knows the colour palette for the Vonduro company logo is: R: 0 G: 86 B: 162 or C: 97% M: 73% Y: 4% K: 0% Thanks Gareth

Hi Designers,

Thanks for all of your submissions to date.  I am working through each design and will provide feedback on all the great work.

One thing I would like to ask is if you could submit a version that has my academic credentials under or after my name.  I am not a big fan of doing this but as I am in business consulting it does seem to be quite common.

I hold a Bachelor of Commerce (BCom) and a Master of Business Administration (MBA)

Thanks

Gareth

Hi Designers,

Thanks for all of your fantastic designs.  There are some really great designs here for my business.  I am still in the process of reviewing designs and should have this completed by tomorrow.  Some of the things I have learnt from this round of designs are:

1) I prefer to have the card without my academic qualifications

2) I really like cards that have a blue back

3) I prefer to have my name and title either left or right of centre

I hope this helps and I will endeavour to get through all of the designs tomorrow

Cheers

Gareth

Target Market(s)

We target large corporate organisations

Industry/Entity Type

Leadership

Requirements
Must have
• Must have the following business details

Gareth Pilling - Director
Address: Level 7, 82 Harlow Street, Melbourne, Australia, 3000
Phone: +61 3 527 840 213
Fax: +61 3 9214 5037
Email: gareth.pilling@vonduro-example.com.au
LinkedIn: au.linkedin.com/in/garethjpilling/
Twiiter: @garethjpilling
Website: www.vonduro-example.com.au

```html
<!DOCTYPE html>
<html lang="en">
<head>
<meta charset="utf-8">
<title>Vonduro Business Card</title>
<link rel="stylesheet" href="https://fonts.googleapis.com/css2?family=Open+Sans:wght@300;400&display=swap">
<style>
  :root {
    --brand-blue: #0056a2;
    --brand-blue-deep: #004c91;
    --ink: #3a3a3a;
    --paper: #ffffff;
    --backdrop: #d4d4d4;
    --rule: #2c6db5;
  }
  * { margin: 0; padding: 0; box-sizing: border-box; }
  html, body {
    width: 1200px; height: 985px; overflow: hidden;
    background: var(--backdrop);
    font-family: "Open Sans", sans-serif;
  }
  .stage {
    position: relative; width: 1200px; height: 985px;
    display: flex; align-items: center; justify-content: center; gap: 40px;
  }
  .card {
    position: relative; width: 500px; height: 290px;
    border-radius: 18px; overflow: hidden;
  }
  .card--front {
    background: var(--brand-blue);
    display: flex; align-items: center; justify-content: center;
  }
  .wordmark {
    font-weight: 300; letter-spacing: 1px; line-height: 1;
  }
  .card--front .wordmark { color: var(--paper); font-size: 58px; }

  .card--back { background: var(--paper); display: flex; }
  .side-band {
    width: 44px; height: 100%;
    background: var(--brand-blue);
    border-right: 4px solid var(--paper);
    box-shadow: 3px 0 0 var(--brand-blue);
    display: flex; flex-direction: column; justify-content: flex-end;
    align-items: center; gap: 6px; padding-bottom: 34px;
  }
  .icon { width: 18px; height: 14px; display: block; }
  .content { padding: 22px 0 0 22px; flex: 1; color: var(--ink); }
  .card--back .wordmark { color: var(--brand-blue); font-size: 44px; margin-bottom: 14px; }
  .name-line {
    display: flex; align-items: baseline; gap: 8px;
    border-bottom: 1px solid var(--rule); padding-bottom: 4px; width: 410px;
  }
  .person-name { color: var(--brand-blue); font-size: 18px; font-weight: 300; }
  .credentials { font-size: 10px; font-weight: 400; color: var(--ink); border-left: 1px solid var(--ink); padding-left: 6px; }
  .role { color: var(--brand-blue); font-size: 12px; font-weight: 300; margin-top: 2px; }
  .details { list-style: none; font-size: 11.5px; font-weight: 300; line-height: 19px; margin-top: 4px; }
</style>
</head>
<body>
<main class="stage">
  <section class="card card--front" aria-label="Card front">
    <span class="wordmark">Vonduro</span>
  </section>

  <section class="card card--back" aria-label="Card back">
    <div class="side-band">
      <svg class="icon" viewBox="0 0 18 14" aria-label="Phone"><rect width="18" height="14" rx="2" fill="#fff"/><path d="M6 3c-1 1-1 3 1 5s4 3 5 2l-1.5-1.5-1 .8-2.6-2.6.8-1z" fill="#0056a2"/></svg>
      <svg class="icon" viewBox="0 0 18 14" aria-label="Fax"><rect width="18" height="14" rx="2" fill="#fff"/><rect x="5" y="4" width="8" height="6" fill="none" stroke="#0056a2"/><line x1="7" y1="6" x2="11" y2="6" stroke="#0056a2"/></svg>
      <svg class="icon" viewBox="0 0 18 14" aria-label="Email"><rect width="18" height="14" rx="2" fill="#fff"/><rect x="4.5" y="4" width="9" height="6" fill="none" stroke="#0056a2"/><path d="M4.5 4 9 7.5 13.5 4" fill="none" stroke="#0056a2"/></svg>
      <svg class="icon" viewBox="0 0 18 14" aria-label="Website"><rect width="18" height="14" rx="2" fill="#fff"/><circle cx="9" cy="7" r="4" fill="none" stroke="#0056a2"/><line x1="5" y1="7" x2="13" y2="7" stroke="#0056a2"/></svg>
      <svg class="icon" viewBox="0 0 18 14" aria-label="Profile"><rect width="18" height="14" rx="2" fill="#fff"/></svg>
      <svg class="icon" viewBox="0 0 18 14" aria-label="Social handle"><rect width="18" height="14" rx="2" fill="#fff"/></svg>
    </div>
    <div class="content">
      <div class="wordmark">Vonduro</div>
      <div class="name-line">
        <span class="person-name">Gareth Pilling</span>
        <span class="credentials">BCom,MBA</span>
      </div>
      <div class="role">Director</div>
      <ul class="details">
        <li>Level 7, 82 Harlow Street, Melbourne, Australia, 3000</li>
        <li>+61 3 527 840 213</li>
        <li>+61 3 9214 5037</li>
        <li>gareth.pilling@vonduro-example.com.au</li>
        <li>www.vonduro-example.com.au</li>
        <li>au.linkedin.com/in/garethjpilling/</li>
        <li>@garethjpilling</li>
      </ul>
    </div>
  </section>
</main>
</body>
</html>
```